ReadNest Learning App for Children with Dyslexia

Project Description:

We are seeking a talented UI/UX designer to create engaging and intuitive designs for Readnest, an innovative educational app designed to help children learn letters and words through a multisensory learning approach. The app aims to be particularly helpful for children with dyslexia, providing a supportive and interactive learning environment.

Key App Features & Design Requirements:

Account Creation Screen: Design a welcoming and straightforward sign-up page that allows users to register with their email or continue with Quorvix. The design should be clean, focusing on user-friendliness and accessibility, adhering to our terms of service and privacy policy.

Main Screen Design: The main screen should allocate at least 4/6 of its height to the interactive drawing area. It needs to display word prompts in both correct and scrambled orders and include options to "Show all Words," "Play all words," and a search function. The interface should be vibrant, engaging, and easy to navigate for children.

Profile Section: Create a user-friendly profile page that allows users to edit their profile image, name, username, email, links, and bio. The design should be clean and encourage user engagement.

NestStats Page: This section will display the user's learning progress, including rankings, a learning curve, and recently learned words. It should visually represent progress in a motivating and understandable way, suitable for a younger audience.

Visual and Auditory Feedback Implementation: Incorporate elements that support visual and auditory feedback, using dyslexia-friendly formats. This includes choosing appropriate colors, fonts, and auditory cues.

Accessibility and Customization Settings: Designs should include settings for adjusting visual contrast, font size, and the word list to accommodate individual preferences and needs.

Feel free to add more interactions and/or pages.

Design preferences:

Color Scheme: Use a bright, inviting color palette that stimulates learning and engagement without overwhelming the users.
Font Selection: Opt for fonts that are readable and accessible, particularly for users with dyslexia.
Icons and Graphics: Design custom icons and graphics that are cohesive with the app's theme and purpose. Illustrations should be simple, relatable, and supportive of the learning process.

Target Market(s)

Educational

Industry/Entity Type

Educational

Colors
0054AA
0677BA
7BADD7
CADEEF
E8F1F8
0094D4
00A9DD
6FCCEA
C7EBF8
E9F6FB

Requirements
Must have
• Educational app, a writing area, scoring and account management
Nice to have
• Statistics, Ranking Page, Settings and some nice visual features

```html
<!DOCTYPE html>
<html lang="en">
<head>
<meta charset="utf-8">
<title>ReadNest – App Screens</title>
<link href="https://fonts.googleapis.com/css2?family=Inter:wght@400;500;600;700;800&display=swap" rel="stylesheet">
<style>
:root{
  --blue:#2467EA;
  --blue-light:#4E95F0;
  --blue-text:#1E63E8;
  --chip:#CFE2FD;
  --chip-soft:#E3EEFD;
  --pad:#EBEEF3;
  --green:#00B552;
  --green-line:#1E9E1E;
  --ink:#1B1B1F;
  --muted:#5B5F66;
  --dark:#2B2B2B;
  --tab:#D4DCEB;
  --page:#F1F3F7;
  --white:#FFFFFF;
}
*{box-sizing:border-box;margin:0;padding:0}
html,body{width:1200px;height:811px;overflow:hidden;background:var(--white);font-family:"Inter",sans-serif;color:var(--ink)}
.canvas{position:relative;width:1200px;height:811px}
.screen{position:absolute;top:147px;width:234px;height:508px;border-radius:26px;overflow:hidden;background:var(--white)}
.abs{position:absolute}
.center{left:0;right:0;text-align:center}

/* sign up */
.signup{left:72px}
.signup .hero{position:absolute;left:0;top:0;width:234px;height:260px}
.brand{top:101px;font-size:28px;font-weight:800;color:var(--white);letter-spacing:.5px}
.tagline{top:135px;font-size:10.5px;font-weight:500;color:var(--white)}
.signup h2{top:259px;font-size:10.5px;font-weight:600}
.signup .lead{top:276px;font-size:7.5px}
.field{left:15px;width:204px;top:302px;height:33px;border:1px solid #C9CCD1;border-radius:17px;display:flex;align-items:center;justify-content:center;font-size:10px;color:#8A8E94}
.btn-green{background:var(--green);color:var(--white);font-weight:600;border-radius:17px;display:flex;align-items:center;justify-content:center}
.signup .continue{left:15px;width:204px;top:344px;height:33px;font-size:10.5px}
.divider{left:18px;width:198px;top:400px;height:1px;background:#E4E6EA}
.divider-label{top:395px;font-size:7.5px}
.divider-label span{background:var(--white);padding:0 6px}
.provider{left:15px;width:204px;top:419px;height:34px;border-radius:17px;background:var(--dark);color:var(--white);font-size:8.5px;display:flex;align-items:center;justify-content:center;gap:8px}
.provider .dot{width:13px;height:13px;border-radius:50%;background:#E9ECF0}
.legal{top:469px;font-size:7.5px;line-height:9.5px}
.legal b{font-weight:600}

/* main */
.main{left:347px}
.main .top{position:absolute;left:0;top:0;width:234px;height:310px;background:linear-gradient(180deg,var(--blue-light),var(--blue));border-radius:0 0 26px 26px}
.menu{left:11px;top:34px}
.main .title{top:33px;font-size:9.5px;font-weight:700;color:var(--white)}
.points{left:171px;top:30px;width:55px;height:20px;border-radius:10px;background:var(--white);font-size:7.5px;font-weight:500;display:flex;align-items:center;justify-content:center;gap:4px}
.coin{width:5px;height:7px;border-radius:2px;background:#F6B90F}
.pad{left:7px;top:64px;width:220px;height:238px;background:var(--pad);border-radius:26px}
.pen{right:10px;bottom:12px}
.segment{left:13px;top:319px;width:207px;height:27px;border:1px solid #C9CCD1;border-radius:14px;display:flex;font-size:8.5px}
.segment span{flex:1;display:flex;align-items:center;justify-content:center;color:#2D2F33}
.segment .on{background:var(--blue);color:var(--white);border-radius:14px;margin:-1px -1px -1px 0}
.chip{position:absolute;display:flex;align-items:center;justify-content:center;background:var(--chip);border-radius:8px;font-size:10.5px;font-weight:500;color:var(--ink)}
.main .chip{width:64px;height:30px}
.main .more{left:58px;top:467px;width:122px;height:26px;border-radius:13px;font-size:8.5px;font-weight:500}

/* profile */
.profile{left:619px;background:linear-gradient(180deg,var(--blue-light),var(--blue))}
.back{left:10px;top:31px}
.profile .title{top:33px;font-size:9px;font-weight:500;color:var(--white)}
.avatar{left:77px;top:58px;width:78px;height:78px;border-radius:50%;background:radial-gradient(circle at 50% 40%,#E9B48C,#C77C4E 55%,#8E9AA7)}
.edit{left:73px;top:145px;width:85px;height:20px;border-radius:10px;background:#111;color:var(--white);font-size:7px;font-weight:500;display:flex;align-items:center;justify-content:center}
.row{position:absolute;left:17px;width:199px;height:33px;border-radius:6px;background:var(--white);display:flex;align-items:center;padding:0 10px 0 16px;font-size:8.5px}
.row .k{flex:1;color:#2D2F33}
.row .v{color:var(--blue-text);font-weight:500;margin-right:8px}
.add{left:17px;top:434px;width:199px;height:33px;border:1px solid var(--white);border-radius:6px;color:var(--white);font-size:8.5px;font-weight:500;display:flex;align-items:center;justify-content:center;gap:14px}

/* stats */
.stats{left:895px;background:var(--page)}
.stats .head{position:absolute;left:0;top:0;width:234px;height:58px;background:linear-gradient(180deg,var(--blue-light),var(--blue))}
.stats .title{top:33px;font-size:7.5px;font-weight:500;color:var(--white)}
.mini-avatar{left:194px;top:26px;width:26px;height:26px;border-radius:50%;background:radial-gradient(circle at 50% 40%,#E9B48C,#C77C4E 60%,#8E9AA7)}
.tab{position:absolute;top:73px;height:18px;border-radius:9px;background:var(--tab);font-size:7px;font-weight:500;display:flex;align-items:center;justify-content:center;color:#2D2F33}
.tab.on{background:var(--blue);color:var(--white)}
.rank{position:absolute;top:107px;width:118px;height:65px;border:1px solid var(--blue-light);border-radius:7px;background:var(--white)}
.rank .lbl{position:absolute;left:10px;top:7px;font-size:7px;font-weight:500;color:var(--blue-text)}
.rank .place{position:absolute;right:9px;top:25px;font-size:16px;font-weight:600;white-space:nowrap}
.rank .of{position:absolute;right:9px;top:43px;font-size:11px;font-weight:500;color:var(--blue-text);white-space:nowrap}
.card{position:absolute;left:8px;width:216px;background:var(--white);border-radius:7px}
.card .lbl{position:absolute;left:10px;top:9px;font-size:7px;font-weight:500;color:var(--blue-text)}
.stats .chip{width:62px;height:29px;border-radius:15px;background:var(--chip-soft)}
</style>
</head>
<body>
<div class="canvas">

  <!-- Sign up -->
  <section class="screen signup">
    <svg class="hero" viewBox="0 0 234 260" aria-hidden="true">
      <defs><linearGradient id="heroFill" x1="0" y1="0" x2="0" y2="1"><stop offset="0" stop-color="#4E95F0"/><stop offset="1" stop-color="#2467EA"/></linearGradient></defs>
      <path d="M0 0H234V236C205 250 180 256 150 252C115 247 95 232 60 234C35 235 15 240 0 242Z" fill="url(#heroFill)"/>
    </svg>
    <div class="abs center brand">READNEST</div>
    <div class="abs center tagline">Learn letters and words</div>
    <h2 class="abs center">Create an account</h2>
    <p class="abs center lead">Enter your email to sign up for this app</p>
    <div class="abs field">email@mailbox.com</div>
    <div class="abs btn-green continue">Continue</div>
    <div class="abs divider"></div>
    <div class="abs center divider-label"><span>or continue with</span></div>
    <div class="abs provider"><span class="dot"></span>Sign in with Quorvix</div>
    <p class="abs center legal">by clicking continue, you agree to our<br><b>Terms of service</b> and <b>Privet Policy</b></p>
  </section>

  <!-- Main -->
  <section class="screen main">
    <div class="top"></div>
    <svg class="abs menu" width="12" height="10" viewBox="0 0 12 10" aria-hidden="true"><path d="M1 1H11M1 5H11M1 9H7" stroke="#fff" stroke-width="1.2" stroke-linecap="round"/></svg>
    <div class="abs center title">READNEST</div>
    <div class="abs points"><span class="coin"></span>16 Points</div>
    <div class="abs pad">
      <svg class="abs pen" width="16" height="16" viewBox="0 0 16 16" aria-hidden="true"><path d="M3 13L5 9L12 2L14 4L7 11Z" fill="#5A8EF0"/><path d="M2 14L3 11L5 13Z" fill="#5A8EF0"/></svg>
    </div>
    <div class="abs segment"><span>Show all words</span><span class="on">Play all words</span></div>
    <div class="chip" style="left:13px;top:362px">word</div>
    <div class="chip" style="left:84px;top:362px">read</div>
    <div class="chip" style="left:155px;top:362px">eat</div>
    <div class="chip" style="left:13px;top:402px">dog</div>
    <div class="chip" style="left:84px;top:402px">cat</div>
    <div class="chip" style="left:155px;top:402px">door</div>
    <div class="abs btn-green more">Show more the result</div>
  </section>

  <!-- Profile -->
  <section class="screen profile">
    <svg class="abs back" width="14" height="10" viewBox="0 0 14 10" aria-hidden="true"><path d="M13 5H1M5 1L1 5L5 9" stroke="#fff" stroke-width="1.2" fill="none" stroke-linecap="round" stroke-linejoin="round"/></svg>
    <div class="abs center title">Profile</div>
    <div class="abs avatar" role="img" aria-label="Profile photo of the user"></div>
    <div class="abs edit">Edit profile image</div>
    <div class="row" style="top:180px"><span class="k">Name</span><span class="v">Mira Dalton</span><svg width="6" height="10" viewBox="0 0 6 10"><path d="M1 1L5 5L1 9" stroke="#333" fill="none"/></svg></div>
    <div class="row" style="top:222px"><span class="k">Username</span><span class="v">@username</span><svg width="6" height="10" viewBox="0 0 6 10"><path d="M1 1L5 5L1 9" stroke="#333" fill="none"/></svg></div>
    <div class="row" style="top:265px"><span class="k">Email</span><span class="v">name@domain</span><svg width="6" height="10" viewBox="0 0 6 10"><path d="M1 1L5 5L1 9" stroke="#333" fill="none"/></svg></div>
    <div class="row" style="top:307px"><span class="k">Bio</span><span class="v">Lorem ipsum is a...</span><svg width="6" height="10" viewBox="0 0 6 10"><path d="M1 1L5 5L1 9" stroke="#333" fill="none"/></svg></div>
    <div class="row" style="top:349px"><span class="k">Web/Links</span><span class="v">website.com</span><svg width="6" height="10" viewBox="0 0 6 10"><path d="M1 1L5 5L1 9" stroke="#333" fill="none"/></svg></div>
    <div class="row" style="top:392px"><span class="k">Web/Links</span><span class="v">website.com</span><svg width="6" height="10" viewBox="0 0 6 10"><path d="M1 1L5 5L1 9" stroke="#333" fill="none"/></svg></div>
    <div class="abs add"><svg width="11" height="11" viewBox="0 0 11 11" aria-hidden="true"><path d="M5.5 0V11M0 5.5H11" stroke="#fff" stroke-width="1.2"/></svg>add new web/link</div>
  </section>

  <!-- Stats -->
  <section class="screen stats">
    <div class="head"></div>
    <svg class="abs back" width="14" height="10" viewBox="0 0 14 10" aria-hidden="true"><path d="M13 5H1M5 1L1 5L5 9" stroke="#fff" stroke-width="1.2" fill="none" stroke-linecap="round" stroke-linejoin="round"/></svg>
    <div class="abs center title">NestStats</div>
    <div class="abs mini-avatar" role="img" aria-label="User avatar photo"></div>
    <div class="tab on" style="left:12px;width:43px">Ranking</div>
    <div class="tab" style="left:63px;width:65px">Correct Words</div>
    <div class="tab" style="left:137px;width:59px">Today words</div>
    <div class="rank" style="left:8px">
      <span class="lbl">Total Ranking</span>
      <svg class="abs" style="left:6px;top:40px" width="20" height="18" viewBox="0 0 20 18" aria-hidden="true"><path d="M5 1H15V6C15 9 13 11 10 11C7 11 5 9 5 6Z" fill="#F6B90F"/><path d="M5 3H2V5C2 7 4 8 5 8M15 3H18V5C18 7 16 8 15 8" stroke="#F6B90F" stroke-width="1.4" fill="none"/><rect x="9" y="11" width="2" height="3" fill="#F6B90F"/><rect x="6" y="14" width="8" height="3" rx="1" fill="#F6B90F"/></svg>
      <span class="place">1st Place</span>
      <span class="of">of 100</span>
    </div>
    <div class="rank" style="left:140px">
      <span class="lbl">Daily Ranking</span>
      <span class="place" style="right:auto;left:19px">10st Place</span>
      <span class="of" style="right:auto;left:65px">of 100</span>
    </div>
    <div class="card" style="top:183px;height:193px">
      <span class="lbl">Learning curve</span>
      <svg class="abs" style="left:0;top:0" width="216" height="193" viewBox="0 0 216 193" font-family="Inter, sans-serif">
        <g stroke="#E3E6EB" stroke-width=".6">
          <line x1="10" y1="35.5" x2="204" y2="35.5"/><line x1="10" y1="52.7" x2="204" y2="52.7"/>
          <line x1="10" y1="70.5" x2="204" y2="70.5"/><line x1="10" y1="87.7" x2="204" y2="87.7"/>
          <line x1="10" y1="104.9" x2="204" y2="104.9"/><line x1="10" y1="122.2" x2="204" y2="122.2"/>
          <line x1="10" y1="139.4" x2="204" y2="139.4"/><line x1="10" y1="156.6" x2="204" y2="156.6"/>
        </g>
        <text x="10" y="43" font-size="4.5" fill="#444">100 words per day</text>
        <text x="10" y="59.5" font-size="4.5" fill="#444">50 words per day</text>
        <path d="M9.4 167C20 168 30 169 36 164C42 158 44 150 50 150C58 151 70 152 77 150C88 147 96 120 106 116C114 113 126 117 132.5 108C142 96 142 65 152 61C158 58 162 60 168 58C180 54 188 45 195 35.5" stroke="var(--green-line)" stroke-width="1.8" fill="none" stroke-linecap="round"/>
        <g font-size="5" fill="#555" text-anchor="middle">
          <text x="19" y="181">Nov 23</text><text x="45" y="181">24</text><text x="71" y="181">25</text>
          <text x="97" y="181">26</text><text x="123" y="181">27</text><text x="149" y="181">28</text>
          <text x="174" y="181">29</text><text x="200" y="181">30</text>
        </g>
      </svg>
    </div>
    <div class="card" style="top:394px;height:130px">
      <span class="lbl">Recently learned words</span>
    </div>
    <div class="chip" style="left:18px;top:424px">word</div>
    <div class="chip" style="left:87px;top:424px">read</div>
    <div class="chip" style="left:155px;top:424px">eat</div>
    <div class="chip" style="left:18px;top:462px">dog</div>
    <div class="chip" style="left:87px;top:462px">cat</div>
    <div class="chip" style="left:155px;top:462px">door</div>
  </section>

</div>
</body>
</html>
```